依頼詳細
現在使っているものを画像データで添付します。
事務所ロゴをフォトショップデータで添付します。

参考に、市販の表紙デザインにはこういったものがあります。(下記リンク)
https://www.kazane-dk.co.jp/store/products/list.php?category_id=23
https://tomoriworks.com/item/certificate/
http://mizuho-kanade.com/front_cover/
A4の紙を綴じるものなので、A3より一回り大きいA3ワイドのレザック紙に印刷しております。こちら302×430mmサイズです。

表紙には、お客様(権利者)の名前と
その下には不動産の表示が入ります。(案件ごとに印刷します)
そのため、こちらを手差し印刷できるよう、高さ5センチ程度の空白を空けておいていただきたいです。

サイズ:A3ワイド(302×430mm)
2つ折り、左開きです。半分に折った部分が表紙となります。

色、デザインの雰囲気等お任せいたします。
公的で固い重要書類をいれるものですが、そういったイメージにはあまり縛られずなるべくオリジナリティのあるものを使いたいと思います。
記載項目
不動産登記権利情報

司法書士ふじさわ事務所
希望イメージ
シンプル 複雑
単色 カラフル
暗い 明るい
日常 高級
遊び心 厳粛
未来的 伝統的
女性的 男性的
希望する色
設定なし
納品ファイル
• イラストレーター形式 (.ai)
補足説明
設定なし
【追記】桐のマークについて
現在使っている権利証表紙には、司法書士バッヂの意匠である五三桐花をいれておりますが、今回は特に使用の指定はしません。
桐のマークを入れる場合については、五三桐でお願いいたします(葉っぱが中央に5枚・左右に3枚ずつの家紋)

(参考)
http://senra-mokudo.com/kamon-c/cate0/kiri/kiri2.html
https://www.ezukan-store.jp/img344/225970_3130817.html
■ 選んだ理由

見た瞬間に目を惹くデザインだと思い、選ばせていただきました。

■ 提案者全員のお礼・コメント

たくさんのご提案をいただき大変嬉しく思っております。
皆様それぞれ、素敵なデザインを考えていただき本当にありがとうございます。

```html
<!DOCTYPE html>
<html lang="ja">
<head>
<meta charset="utf-8">
<title>不動産登記権利情報 表紙</title>
<link rel="stylesheet" href="https://fonts.googleapis.com/css2?family=Noto+Serif+JP:wght@400;600;700&display=swap">
<style>
  :root{
    --cover-blue:#7f98b6;
    --frame-silver:#d2d8e0;
    --frame-gold:#c9b27a;
    --ink:#1b1e24;
    --box-line:#34445f;
    --paper-white:#ffffff;
  }
  *{margin:0;padding:0;box-sizing:border-box}
  html,body{width:849px;height:1200px;overflow:hidden}
  body{background:var(--cover-blue);font-family:"Noto Serif JP",serif;position:relative}
  .cover{position:absolute;inset:0;width:849px;height:1200px}
  .frame{position:absolute;left:0;top:0}
  .crest{position:absolute;left:404px;top:30px;width:40px;height:40px;border-radius:50%;
    background:radial-gradient(circle,var(--frame-silver),#aab4c2)}
  .corner{position:absolute;width:46px;height:46px;background:var(--frame-gold);opacity:.55}
  .corner.tl{left:40px;top:34px}
  .corner.tr{right:40px;top:34px}
  .corner.bl{left:40px;top:818px}
  .corner.br{right:40px;top:818px}
  .title{position:absolute;left:0;width:849px;top:142px;text-align:center;
    font-size:40px;font-weight:600;color:var(--ink);letter-spacing:5px;line-height:1.2}
  .title-rule{position:absolute;left:198px;width:453px;top:204px;height:1.5px;background:var(--ink)}
  .entry-box{position:absolute;border:1.5px solid var(--box-line)}
  .entry-box.holder{left:86px;top:325px;width:672px;height:94px}
  .entry-box.property{left:226px;top:464px;width:397px;height:192px}
  .office{position:absolute;left:113px;top:910px;display:flex;align-items:flex-start;gap:85px;color:var(--paper-white)}
  .office-mark{width:85px;height:85px;background:var(--paper-white);flex:none}
  .office-role{font-size:40px;font-weight:700;letter-spacing:18px;line-height:1.2;white-space:nowrap}
  .office-name{font-size:52px;font-weight:700;letter-spacing:23px;line-height:1.3;margin-top:8px;white-space:nowrap}
  .contact{position:absolute;left:240px;color:var(--paper-white);font-size:14px;letter-spacing:1px;white-space:nowrap}
  .contact.address{top:1080px}
  .contact.phone{top:1118px}
  .contact.phone span{margin-right:18px}
</style>
</head>
<body>
<main class="cover">
  <svg class="frame" width="849" height="1200" viewBox="0 0 849 1200" aria-hidden="true">
    <rect x="54" y="46" width="741" height="808" fill="none" stroke="var(--frame-silver)" stroke-width="2"/>
    <rect x="64" y="56" width="721" height="788" fill="none" stroke="var(--frame-silver)" stroke-width="1"/>
    <line x1="120" y1="50" x2="380" y2="50" stroke="var(--frame-gold)" stroke-width="1.5"/>
    <line x1="469" y1="50" x2="729" y2="50" stroke="var(--frame-gold)" stroke-width="1.5"/>
  </svg>
  <div class="crest" role="img" aria-label="上部中央の円形飾り"></div>
  <div class="corner tl" role="img" aria-label="四隅の飾り模様"></div>
  <div class="corner tr" role="img" aria-label="四隅の飾り模様"></div>
  <div class="corner bl" role="img" aria-label="四隅の飾り模様"></div>
  <div class="corner br" role="img" aria-label="四隅の飾り模様"></div>

  <h1 class="title">不動産登記権利情報</h1>
  <div class="title-rule"></div>

  <div class="entry-box holder"></div>
  <div class="entry-box property"></div>

  <div class="office">
    <div class="office-mark"></div>
    <div class="office-text">
      <p class="office-role">司法書士・行政書士</p>
      <p class="office-name">ふじさわ事務所</p>
    </div>
  </div>
  <p class="contact address">〒060-0012　北海道架空市中央町3丁目12番地</p>
  <p class="contact phone"><span>TEL：0123-45-6780</span><span>FAX：0123-45-6781</span></p>
</main>
</body>
</html>
```